Business Card Design

business service ; plasterboard /plastering/suspended ceiling /partition wall /ceiling restoration specialist

Industry/Entity Type

Business Service

Contact Information for Business Card

campany name tkr interiors
director name rolf
0461927305 email tkrinteriors@quillpost.com.au

Requirements
Must have
• please put my business service

```html
<!DOCTYPE html>
<html lang="en">
<head>
<meta charset="utf-8">
<title>TKR Interiors Pty Ltd – Business Card</title>
<link rel="stylesheet" href="https://fonts.googleapis.com/css2?family=Tinos&family=PT+Sans:wght@700&display=swap">
<style>
  :root {
    --card-light: #f9f9fa;
    --card-mid: #eeeff0;
    --card-shade: #e4e5e7;
    --name-ink: #2b2b2d;
    --mark-blue: #3d74b4;
    --service-grey: #a6a8ab;
  }
  * { margin: 0; padding: 0; box-sizing: border-box; }
  html, body {
    width: 1200px;
    height: 742px;
    overflow: hidden;
    background: var(--card-mid);
  }
  .card {
    position: relative;
    width: 1200px;
    height: 742px;
    background: radial-gradient(ellipse at 78% 18%, var(--card-light) 0%, var(--card-mid) 55%, var(--card-shade) 100%);
    font-family: "Tinos", "Times New Roman", serif;
  }
  .brand-mark {
    position: absolute;
    top: 262px;
    left: 0;
    width: 1200px;
    display: flex;
    justify-content: center;
    align-items: center;
    gap: 18px;
  }
  .brand-mark__name {
    font-family: "Tinos", "Times New Roman", serif;
    font-size: 132px;
    line-height: 1;
    letter-spacing: 6px;
    color: var(--mark-blue);
  }
  .company-name {
    position: absolute;
    top: 478px;
    left: 0;
    width: 1200px;
    text-align: center;
    font-family: "Tinos", "Times New Roman", serif;
    font-size: 45px;
    letter-spacing: 5.6px;
    color: var(--name-ink);
    text-transform: uppercase;
  }
  .services {
    position: absolute;
    top: 620px;
    left: 0;
    width: 1200px;
    text-align: center;
    font-family: "PT Sans", "Arial Narrow", sans-serif;
    font-weight: 700;
    font-size: 31px;
    line-height: 41px;
    color: var(--service-grey);
  }
  .services__divider {
    display: inline-block;
    margin: 0 10px;
  }
</style>
</head>
<body>
  <main class="card">
    <div class="brand-mark">
      <span class="brand-mark__name">TKR</span>
    </div>
    <h1 class="company-name">tkr interiors pty ltd</h1>
    <div class="services">
      <p class="services__line">plasterboard<span class="services__divider">|</span>plastering<span class="services__divider">|</span>suspended ceiling</p>
      <p class="services__line">partition wall<span class="services__divider">|</span>ceiling restoration specialist</p>
    </div>
  </main>
</body>
</html>
```